wardrobe/costume stylist needs good business card for own business

Hi:)

I'm wanting a business card for my company. I am a freelance stylist.

I do wardrobe/costume stylist to TV commercials; Films; Fashion and Lifestyle shoots.

I'd like a design based around my name Rosalind Pember written nicely, maybe a colour? Up to you?!

I've attached a couple of images of business cards I like
.... be creative and have fun!

Thank you :)
Updates

Reason: I was trying to get my new business card ready for before I headed overseas Friday morning but I don't think that was realistic so I'd like to extend the deadline to give time to the project. Thank you

Hi designers:) Thank you for all your designs, I've extended the deadline until Sunday, so there's a bit more time. I've attached 3 pictures of business cards which I quite like, please take a look to see if it can be of help in your process. I like the pale plain or patterned background with dark font and the dark plain or patterned background with the pale font the motifs the feminine fonts the plain fonts I like the idea of playing with a circle or some shape on one side of the card with my name or initials as in the picture I have on my post could you play around with this idea a bit please? Thank you all for the work you've done :) Rosa

Hi I am working overseas til Saturday night sorry for no feedback until I teturn Thanks :) Rosa

Hi designers, Thank you all so much for submitting your designs, I really appreciate your input into my project :) I'm sorry I didn't get to respond to some comments, and give feedback. I didn't back from being away until later than I expected, and the deadline had passed then, so apologies. Thanks to you all again for all your really good designs :) Rosa

Target Market(s)

I am a freelance stylist my target audience is producers, production companies, photographers, directors...

Industry/Entity Type

Business

Requirements
Must have
• Rosalind Pember
Stylist or Wardrobe Stylist

email rosapember@quillnet.co.nz
Mobile 0218846193

(Don't have to use the words 'email' and 'mobile')
Nice to have
• Would like it to be double sided
Like B & W
Like pale colour background with dark font or white font
Like dark colour background with pale font
Should not have
• I would prefer it not to incorporate pictures

```html
<!DOCTYPE html>
<html lang="en">
<head>
<meta charset="utf-8">
<title>Rosalind Pember — Stylist Business Card</title>
<link rel="stylesheet" href="https://fonts.googleapis.com/css2?family=Pacifico&family=Dancing+Script:wght@500;600&display=swap">
<style>
  :root {
    --backdrop: #e9e6e3;
    --rose: #c7a398;
    --paper: #f7f6f4;
    --ink-white: #ffffff;
    --ink-rose: #c29a8e;
    --ornament-light: #ffffff;
    --ornament-soft: #ead9d3;
    --card-shadow: 0 10px 28px rgba(60, 40, 30, 0.18);
  }
  * { margin: 0; padding: 0; box-sizing: border-box; }
  html, body {
    width: 1200px;
    height: 900px;
    overflow: hidden;
    background: var(--backdrop);
  }
  .canvas {
    width: 1200px;
    height: 900px;
    display: flex;
    flex-direction: column;
    align-items: center;
    justify-content: center;
    gap: 60px;
  }
  .card {
    position: relative;
    width: 600px;
    height: 300px;
    overflow: hidden;
    box-shadow: var(--card-shadow);
  }

  /* Front */
  .card--front { background: var(--rose); }
  .card__ornament {
    position: absolute;
    width: 96px;
    height: 150px;
  }
  .card__ornament--left {
    left: 0;
    bottom: 0;
    background: linear-gradient(90deg, var(--ornament-light) 0%, var(--ornament-soft) 100%);
  }
  .card__ornament--right {
    right: 0;
    top: 0;
    background: linear-gradient(270deg, var(--ornament-light) 0%, var(--ornament-soft) 100%);
  }
  .card__identity {
    position: absolute;
    left: 96px;
    right: 96px;
    top: 0;
    bottom: 0;
    display: flex;
    flex-direction: column;
    align-items: center;
    justify-content: center;
    color: var(--ink-white);
    text-align: center;
  }
  .card__name {
    font-family: "Pacifico", cursive;
    font-weight: 400;
    font-size: 42px;
    line-height: 1.25;
    white-space: nowrap;
  }
  .card__role {
    font-family: "Dancing Script", cursive;
    font-weight: 600;
    font-size: 20px;
    line-height: 1;
    margin-top: 2px;
    margin-left: 110px;
  }

  /* Back */
  .card--back {
    background: var(--paper);
    display: flex;
    align-items: center;
    justify-content: center;
  }
  .card__contact {
    font-family: "Dancing Script", cursive;
    font-weight: 500;
    color: var(--ink-rose);
    text-align: center;
    font-style: italic;
    line-height: 1.2;
  }
  .card__email {
    font-size: 30px;
    letter-spacing: 1px;
    white-space: nowrap;
  }
  .card__phone {
    font-size: 36px;
    letter-spacing: 3px;
  }
</style>
</head>
<body>
  <main class="canvas">
    <section class="card card--front">
      <div class="card__ornament card__ornament--left" role="img" aria-label="White sketched flower ornament at the lower left corner"></div>
      <div class="card__ornament card__ornament--right" role="img" aria-label="White sketched flower ornament at the upper right corner"></div>
      <div class="card__identity">
        <h1 class="card__name">Rosalind Pember</h1>
        <p class="card__role">stylist</p>
      </div>
    </section>

    <section class="card card--back">
      <div class="card__contact">
        <p class="card__email">rosapember@quillnet.co.nz</p>
        <p class="card__phone">0218846193</p>
      </div>
    </section>
  </main>
</body>
</html>
```